Clearbrook Lawnworks LLC Business Card

Ok, first off let me thank you for taking the time to participate in this project !! I have my business logo that I want incorporated into business card design . My irrigation business is located in a very upscale part of town and we do high end homes . So with that said I'm planning on these cards being plastic credit card type cards. I would like them to be two sided . I'm thinking something bold , yet classy and clean . Not too busy . We do different types of work . 80% irrigation service and installation . 15% landscape lighting and the other 5% drainage and hardscapes ! I have a website that I want listed on it as well as our address , phone number and of course my name and title .

Target Market(s)

Upscale homeowners and architects

Industry/Entity Type

Landscape

Requirements
Must have
• Company logo, website, address , phone number , name , title , services offered

Www.ClearbrookLawnworks.example
Marcus Hendley owner
205-555-0148
Clearbrook Lawnworks LLC
P.O. Box 478512
Birmingham, Alabama 35213

```html
<!DOCTYPE html>
<html lang="en">
<head>
<meta charset="utf-8">
<title>Clearbrook Lawnworks LLC Business Card</title>
<link rel="stylesheet" href="https://fonts.googleapis.com/css2?family=Arimo:wght@400;700&display=swap">
<style>
  :root {
    --paper: #ffffff;
    --lawn: #84e800;
    --brand-green: #4cc418;
    --mark-green: #6fcf1a;
    --service-green: #8edc4a;
    --water-blue: #2a8fd8;
    --trim-orange: #f0961e;
    --bleed-magenta: #e020e0;
    --owner-green: #3f9a2a;
  }
  html, body {
    margin: 0;
    padding: 0;
    width: 817px;
    height: 1200px;
    overflow: hidden;
    background: var(--paper);
  }
  .card-sheet {
    display: block;
    width: 817px;
    height: 1200px;
    font-family: "Arimo", Arial, sans-serif;
  }
  .bleed-edge { fill: var(--paper); stroke: var(--bleed-magenta); stroke-width: 1.5; }
  .lawn-band { fill: var(--lawn); }
  .safe-frame { fill: none; stroke: var(--trim-orange); stroke-width: 2.5; }
  .brand-dot { fill: var(--water-blue); }
  .brand-name { fill: var(--mark-green); font-weight: 700; font-size: 44px; }
  .contact-line { fill: var(--paper); font-size: 25px; }
  .company-title { fill: var(--brand-green); font-weight: 700; font-size: 31px; }
  .owner-name { fill: var(--brand-green); font-weight: 700; font-size: 27px; }
  .owner-role { fill: var(--owner-green); font-size: 24px; }
  .service-list { fill: var(--service-green); font-size: 24px; }
  .address-line { fill: var(--paper); font-size: 25px; }
</style>
</head>
<body>
<svg class="card-sheet" viewBox="0 0 817 1200" xmlns="http://www.w3.org/2000/svg">
  <defs>
    <linearGradient id="rain-wash" x1="0" y1="0" x2="1" y2="1">
      <stop offset="0" stop-color="#eef8fc"/>
      <stop offset="1" stop-color="#ffffff"/>
    </linearGradient>
  </defs>

  <g class="card-front">
    <rect class="bleed-edge" x="1" y="1" width="814" height="533"/>
    <path class="lawn-band" d="M1 292 C 200 400, 560 405, 815 296 L 815 534 L 1 534 Z"/>
    <rect class="safe-frame" x="29" y="29" width="761" height="480" rx="33"/>
    <circle class="brand-dot" cx="408" cy="180" r="72"/>
    <text class="brand-name" x="408" y="305" text-anchor="middle">Clearbrook Lawnworks</text>
    <text class="contact-line" x="408" y="420" text-anchor="middle">Www.ClearbrookLawnworks.example</text>
    <text class="contact-line" x="408" y="455" text-anchor="middle">205-555-0148</text>
  </g>

  <g class="card-back">
    <rect class="bleed-edge" x="1" y="663" width="814" height="533"/>
    <rect x="2" y="664" width="812" height="420" fill="url(#rain-wash)" role="img" aria-label="Faint diagonal rain streak texture"/>
    <path class="lawn-band" d="M1 948 C 250 1090, 570 1090, 815 955 L 815 1196 L 1 1196 Z"/>
    <rect class="safe-frame" x="29" y="692" width="761" height="476" rx="33"/>
    <text class="company-title" x="408" y="800" text-anchor="middle">Clearbrook Lawnworks LLC</text>
    <text class="owner-name" x="408" y="857" text-anchor="middle">Marcus Hendley</text>
    <text class="owner-role" x="408" y="889" text-anchor="middle">(Owner)</text>
    <text class="service-list" text-anchor="middle">
      <tspan x="408" y="940">Our services include irrigation</tspan>
      <tspan x="408" y="972">service and installation, landscape</tspan>
      <tspan x="408" y="1004">lighting, drainage and hardscapes.</tspan>
    </text>
    <text class="address-line" x="408" y="1109" text-anchor="middle">P.O. Box 478512, Birmingham, Alabama 35213</text>
  </g>
</svg>
</body>
</html>
```